facial aesthetics advertising dermal fillers for lip and facial rejuvenation

the poster(s) is to engage the interest of patients in a dental surgery. I am introducing new service and wish to attract interest and increase bookings. the service is facial rejuvenation using dermal fillers to reinstore youthfulness vitality and lost volume to the ageing female and male patients as well as to volumise lips in those patients who want fuller lips. upon seeing the poster the patient should feel positive
Updates

Reason: Looking for a client-pulling stand out design which communicates effectively the service of facial rejuvenation, restoration of vitality and returning patients their self-confidence. Graphics need to be of realistic men and women who are aged mid 30 onwards. Images should also include before and after treatments. These images can be sent over if required. Please see original brief for other details Many thanks for reading through and helping the cause.

Target Market(s)

18-65+

Industry/Entity Type

Dental

Colors

Designer to choose colors to be used in the design.

Requirements
Must have
• 1.clear images of female at forefront (perhaps male in the background looking happily at the woman) attractive features
• full lips
• age perhaps mid 30s
• 2. pre and post dermal filler treatment poster.
Nice to have
• eye catching but not brash
• sophisticated and positive

```html
<!DOCTYPE html>
<html lang="en">
<head>
<meta charset="utf-8">
<title>Facial Aesthetics Poster</title>
<link href="https://fonts.googleapis.com/css2?family=Jost:wght@400;500;600&display=swap" rel="stylesheet">
<style>
  :root {
    --page-bg: #e6eaef;
    --ink: #111318;
    --text: #2b2d33;
    --purple: #a4119f;
    --teal: #2aa89c;
    --teal-deep: #24978c;
    --white: #ffffff;
  }
  html, body {
    margin: 0;
    width: 1200px;
    height: 900px;
    overflow: hidden;
    background: var(--page-bg);
    font-family: "Jost", sans-serif;
  }
  .poster {
    position: absolute;
    left: 40px;
    top: 200px;
    width: 1120px;
    height: 500px;
    overflow: hidden;
    box-shadow: 0 6px 24px rgba(20, 30, 50, 0.18);
  }
  .poster-art {
    position: absolute;
    inset: 0;
    width: 1120px;
    height: 500px;
  }
  .headline {
    position: absolute;
    left: 78px;
    top: 42px;
    margin: 0;
    font-weight: 400;
    font-size: 35px;
    line-height: 44px;
    letter-spacing: 0.4px;
    color: var(--ink);
    text-transform: uppercase;
  }
  .headline .accent {
    color: var(--purple);
    font-weight: 600;
  }
  .headline .strong { font-weight: 600; }
  .benefits {
    position: absolute;
    left: 315px;
    top: 218px;
    margin: 0;
    padding: 0;
    list-style: none;
    font-size: 20px;
    line-height: 26px;
    color: var(--text);
    font-weight: 500;
  }
  .benefits li {
    position: relative;
    padding-left: 30px;
    margin-bottom: 5px;
  }
  .benefits svg {
    position: absolute;
    left: 0;
    top: 5px;
    width: 20px;
    height: 16px;
  }
  .booking {
    position: absolute;
    left: 78px;
    top: 462px;
    margin: 0;
    font-size: 24px;
    line-height: 28px;
    font-weight: 600;
    letter-spacing: 0.6px;
    color: var(--white);
  }
</style>
</head>
<body>
  <main class="poster">
    <svg class="poster-art" viewBox="0 0 1120 500" xmlns="http://www.w3.org/2000/svg">
      <defs>
        <linearGradient id="board-sheen" x1="0" y1="0" x2="1" y2="1">
          <stop offset="0" stop-color="#fbfcfd"/>
          <stop offset="1" stop-color="#e9edf2"/>
        </linearGradient>
        <linearGradient id="portrait-tones" x1="0" y1="0" x2="1" y2="0">
          <stop offset="0" stop-color="#c79a80"/>
          <stop offset="0.45" stop-color="#e3b9a0"/>
          <stop offset="1" stop-color="#f2d6c6"/>
        </linearGradient>
        <linearGradient id="model-tones" x1="0" y1="0" x2="0" y2="1">
          <stop offset="0" stop-color="#8a5a3c"/>
          <stop offset="0.35" stop-color="#eec7b0"/>
          <stop offset="1" stop-color="#f4dccd"/>
        </linearGradient>
      </defs>

      <rect class="board-bg" width="1120" height="500" fill="url(#board-sheen)"/>

      <path class="portrait-photo" role="img"
            aria-label="Before and after portrait: a man in profile behind a woman facing forward, her skin peeling back to show the treated side"
            d="M700,0 L1120,0 L1120,500 L790,500 Q740,420 705,330 Q675,220 682,120 Q688,50 700,0 Z"
            fill="url(#portrait-tones)"/>

      <rect class="model-photo" role="img"
            aria-label="Woman touching her chin, with arrows marking lifting lines on her face"
            x="125" y="205" width="180" height="260" rx="70" fill="url(#model-tones)"/>

      <path class="band-purple"
            d="M0,280 C220,400 450,440 700,440 Q745,440 770,470 L740,456 L700,456 C450,456 220,420 0,320 Z"
            fill="var(--purple)"/>
      <path class="band-teal"
            d="M0,320 C220,420 450,456 700,456 Q765,456 790,500 L0,500 Z"
            fill="var(--teal)"/>
      <path class="band-teal-shade"
            d="M0,370 C240,460 480,488 760,492 L765,500 L0,500 Z"
            fill="var(--teal-deep)" opacity="0.5"/>
    </svg>

    <h1 class="headline">
      Anti-wrinkle <span class="accent">Treatment</span><br>
      <span class="accent">Dermal Fillers</span> for <span class="accent">Lip</span> <span class="strong">and</span><br>
      Facial <span class="accent">Rejuvenation</span>
    </h1>

    <ul class="benefits">
      <li><svg viewBox="0 0 20 16"><path d="M2,8 L7,13 L18,2" fill="none" stroke="var(--purple)" stroke-width="2.5"/></svg>Restore vitality naturally</li>
      <li><svg viewBox="0 0 20 16"><path d="M2,8 L7,13 L18,2" fill="none" stroke="var(--purple)" stroke-width="2.5"/></svg>To lift your self-confidence</li>
      <li><svg viewBox="0 0 20 16"><path d="M2,8 L7,13 L18,2" fill="none" stroke="var(--purple)" stroke-width="2.5"/></svg>Bring out the best you</li>
      <li><svg viewBox="0 0 20 16"><path d="M2,8 L7,13 L18,2" fill="none" stroke="var(--purple)" stroke-width="2.5"/></svg>Linden street trained<br>professional</li>
    </ul>

    <p class="booking">Enquire at reception to book with Dr Amara</p>
  </main>
</body>
</html>
```